Envelope design

We need a envelope design for a professional services firm called Brindlemoor Tax Consultancy Inc. The firm is essentially a very specialized tax accounting firm - instead of serving the end consumer, we support other public accounting firms in the area of Canadian and U.S. tax advisory and compliance (i.e. they call us on tax issues too complex for the general practitioner). Our byline is "Tax Support Services for Public Accounting Firms". Our postcard should utilize our logo and be based on colours present in our logo (see file attached). The final design needs to convey professionalism and trustworthiness (we're hired by accountants after all!) while being creative and eye-catching. Eye-catching is critical, since many prospective recipients will not have heard from me before and I want them to read the postcard.
At lot of design work has already been done here. I've attached a number of sample files showing logo and letterhead designs. Please note that the letterhead hasn't yet been updated for the new logo. This is happening in a separate design competition.
Updates
Project Deadline Extended Reason: Deadline is extended because I am pricing the extra cost of having colour right to the edge of the envelopes. This will help me design on final design. Pricing should come in on Monday. Added Saturday, February 20, 2016

```html
<!DOCTYPE html>
<html lang="en">
<head>
<meta charset="utf-8">
<title>Brindlemoor Tax Consultancy – Envelope</title>
<link href="https://fonts.googleapis.com/css2?family=Arimo&family=Open+Sans:wght@400&display=swap" rel="stylesheet">
<style>
  :root {
    --backdrop: #3d2617;
    --ink-black: #151515;
    --paper: #ffffff;
    --brand-orange: #f0a233;
    --brand-navy: #1f4a78;
    --brand-blue: #3e78b0;
    --label: #ffffff;
    --small-text: #333333;
    --flap-line: #2a2a2a;
  }
  html, body {
    margin: 0; padding: 0;
    width: 1200px; height: 1000px;
    overflow: hidden;
    background: var(--backdrop);
  }
  .board { position: relative; width: 1200px; height: 1000px; }
  .view-label {
    position: absolute; left: 17px; margin: 0;
    font-family: "Arimo", Arial, sans-serif;
    font-size: 57px; line-height: 72px; font-weight: 400;
    color: var(--label);
  }
  .label-front { top: 120px; }
  .label-closed { top: 397px; }
  .label-open { top: 772px; }

  .envelope {
    position: absolute; left: 287px; width: 653px;
    background: var(--paper);
    box-shadow: 0 2px 6px rgba(0,0,0,.45);
  }
  .envelope-front { top: 10px; height: 283px; }
  .envelope-back-closed { top: 304px; height: 283px; }
  .envelope-back-open { top: 604px; height: 386px; background: transparent; box-shadow: none; }

  .front-band {
    height: 89px; background: var(--ink-black);
    display: flex; align-items: center; justify-content: center;
  }
  .company-name {
    margin: 0;
    font-family: "Open Sans", Arial, sans-serif;
    font-size: 26px; font-weight: 400; line-height: 32px;
    color: var(--paper);
  }

  .return-address {
    position: absolute; left: 0; right: 0; bottom: 3px;
    text-align: center;
    font-family: "Open Sans", Arial, sans-serif;
    font-style: normal;
    font-size: 7.5px; line-height: 13px; color: var(--small-text);
  }

  .closed-flap {
    height: 102px; background: var(--ink-black);
    border-radius: 0 0 30px 30px;
  }

  .open-flap {
    position: absolute; left: 0; top: 0; width: 653px; height: 172px;
    border-radius: 22px 22px 0 0;
    background: linear-gradient(135deg, var(--brand-orange) 0%, var(--brand-blue) 50%, var(--brand-navy) 100%);
  }
  .envelope-body {
    position: absolute; left: 0; top: 102px; width: 653px; height: 284px;
    background: var(--paper);
    box-shadow: 0 2px 6px rgba(0,0,0,.45);
  }
  .inner-liner {
    position: absolute; left: 6px; top: 102px; width: 641px; height: 70px;
    border-radius: 0 0 22px 22px;
    background: linear-gradient(135deg, var(--brand-orange) 0%, var(--brand-blue) 55%, var(--brand-navy) 100%);
    border: 1px solid var(--flap-line); border-top: none;
    box-sizing: border-box;
  }
</style>
</head>
<body>
<main class="board">
  <p class="view-label label-front">Front</p>
  <p class="view-label label-closed">Back -<br>Close</p>
  <p class="view-label label-open">Back -<br>Open</p>

  <section class="envelope envelope-front" aria-label="Envelope front">
    <header class="front-band">
      <h1 class="company-name">Brindlemoor Tax Consultancy Inc.</h1>
    </header>
    <address class="return-address">
      18-410 Harrowgate Road, Millbrook, Nova Scotia, Canada B0X 2K4<br>
      T: 902.555.0148 &nbsp;|&nbsp; F: 902.555.0172 &nbsp;|&nbsp; E: owen@brindlemoortax.services<br>
      www.brindlemoortax.services
    </address>
  </section>

  <section class="envelope envelope-back-closed" aria-label="Envelope back, flap closed">
    <div class="closed-flap"></div>
  </section>

  <section class="envelope envelope-back-open" aria-label="Envelope back, flap open">
    <div class="open-flap" role="img" aria-label="Repeating brand pattern in orange, blue and navy on the open flap"></div>
    <div class="envelope-body"></div>
    <div class="inner-liner" role="img" aria-label="Repeating brand pattern lining inside the envelope"></div>
  </section>
</main>
</body>
</html>
```